Tov Fiesta Mariners

We are party planning business. We are a team of established individuals and business in party stream businesses like DJ, Caterers, Party supplies, Kids parties, Events & Private Parties and much more. So basically me and business collaborate a team of business or individuals to do clients party in the best way possible.

Target Market(s)

majority of them 16 to 30 -60% to 70 % and 30 to 40 year olds- 30% to 40 %

Industry/Entity Type

Party Planning

Contact Information for Business Card

Tov
Owner & Manager
0471829354
tovfiestamariners@mailpost.example

Requirements
Must have
• front side : Logo and list of services we provide
DJ's, Catering,All party supplies, Tinyjubilee and more...just to show what the business is about when anyone looks at the card and at the rear side my details which are already provided.
Should not have
• Dont make it look we do kids party which is just one of the things we do but don't make my business card look like kids party specialist make it more connecting to youngsters and older crowd more

```html
<!DOCTYPE html>
<html lang="en">
<head>
<meta charset="utf-8">
<title>Tov Fiesta Mariners – Business Cards</title>
<link rel="stylesheet" href="https://fonts.googleapis.com/css2?family=Uncial+Antiqua&family=Pirata+One&display=swap">
<style>
  :root {
    --bg: #2b2b2b;
    --card-black: #0d0d0d;
    --card-white: #ffffff;
    --pirate-red: #d4161c;
    --ink: #141414;
    --soft-white: #f2f2f2;
  }
  * { box-sizing: border-box; margin: 0; padding: 0; }
  html, body { width: 1200px; height: 900px; overflow: hidden; }
  body { background: var(--bg); position: relative; font-family: "Uncial Antiqua", serif; }

  .card {
    position: absolute;
    left: 250px;
    width: 700px;
    height: 400px;
    overflow: hidden;
    box-shadow: 0 10px 30px rgba(0,0,0,.5);
  }

  /* ---------- Front: brand & services ---------- */
  .card--front { top: 30px; background: var(--card-black); }
  .brand-disc {
    position: absolute; left: -70px; top: -40px;
    width: 480px; height: 480px; border-radius: 50%;
    background: var(--card-white);
  }
  .brand-disc__ring {
    position: absolute; inset: 16px; border-radius: 50%;
    border: 4px solid var(--pirate-red);
  }
  .brand-mark {
    position: absolute; left: 185px; top: 105px;
    width: 60px; height: 60px; border-radius: 50%;
    background: var(--pirate-red);
  }
  .brand-name {
    position: absolute; left: 20px; top: 190px; width: 390px;
    text-align: center; color: var(--pirate-red);
    font-weight: 400; font-size: 40px; line-height: 1.1;
  }
  .services {
    position: absolute; left: 440px; top: 52px;
    list-style: none; font-size: 23px; line-height: 42px;
    white-space: nowrap;
  }
  .services li { color: var(--soft-white); }
  .services li::before { content: "★"; color: var(--pirate-red); font-size: 13px; margin-right: 6px; vertical-align: middle; }
  .services li.is-red { color: var(--pirate-red); }
  .services li.is-red::before { color: var(--soft-white); }

  /* ---------- Back: contact details ---------- */
  .card--back { top: 470px; background: var(--card-white); }
  .accent-disc {
    position: absolute; left: -230px; top: 70px;
    width: 470px; height: 470px; border-radius: 50%;
    background: var(--card-black);
  }
  .accent-disc__ring {
    position: absolute; inset: 12px; border-radius: 50%;
    border: 4px solid var(--pirate-red);
  }
  .contact {
    position: absolute; left: 260px; top: 30px; width: 420px;
    text-align: center; color: var(--ink);
  }
  .contact__name { font-family: "Pirata One", serif; font-weight: 400; color: var(--pirate-red); font-size: 62px; line-height: 1; }
  .contact__role { font-size: 24px; margin-top: 6px; }
  .contact__icons { margin: 18px 0 20px; display: flex; justify-content: center; align-items: center; gap: 22px; }
  .contact__phone { font-size: 26px; }
  .contact__email { font-size: 17px; margin-top: 18px; white-space: nowrap; }
</style>
</head>
<body>

  <section class="card card--front" aria-label="Business card front">
    <div class="brand-disc"><div class="brand-disc__ring"></div></div>
    <div class="brand-mark" aria-hidden="true"></div>
    <h1 class="brand-name">Tov Fiesta<br>Mariners</h1>
    <ul class="services">
      <li>DJ</li>
      <li class="is-red">Caterers</li>
      <li>Party supplies</li>
      <li class="is-red">Kids parties</li>
      <li>Events</li>
      <li class="is-red">Private Parties</li>
      <li>and much more</li>
    </ul>
  </section>

  <section class="card card--back" aria-label="Business card back">
    <div class="accent-disc"><div class="accent-disc__ring"></div></div>
    <div class="contact">
      <h2 class="contact__name">TOV</h2>
      <p class="contact__role">Owner and Manager</p>
      <div class="contact__icons" aria-hidden="true">
        <svg width="22" height="26" viewBox="0 0 22 26"><ellipse cx="7" cy="20" rx="6" ry="4" fill="#d4161c"/><rect x="11" y="2" width="2.5" height="18" fill="#d4161c"/></svg>
        <svg width="34" height="34" viewBox="0 0 24 24"><path d="M12 1l3.1 7.2 7.9.7-6 5.2 1.8 7.7L12 17.8 5.2 21.8 7 14.1 1 8.9l7.9-.7z" fill="#141414"/></svg>
        <svg width="24" height="28" viewBox="0 0 24 28"><ellipse cx="7" cy="22" rx="6" ry="4" fill="#d4161c"/><rect x="11" y="3" width="2.5" height="19" fill="#d4161c"/><path d="M13.5 3c4 1 7 3 8 7-2-2-5-3-8-3z" fill="#d4161c"/></svg>
      </div>
      <p class="contact__phone">0471829354</p>
      <p class="contact__email">tovfiestamariners@mailpost.example</p>
    </div>
  </section>

</body>
</html>
```